Crestline Gas and Plumbing Business Card Design

I am after a business card design for my plumbing business called 'Crestline Gas & Plumbing'. I do all types of plumbing and gas work and specialise in general maintenance plumbing. Would like to see designs using current logo

Industry/Entity Type

Plumbing

Contact Information for Business Card

Name - Dale Whitcombe
Phone number - 0455163027
Email - admin@crestlinegasandplumbing.example.com.au
ABN - 68204915336

```html
<!DOCTYPE html>
<html lang="en">
<head>
<meta charset="utf-8">
<title>Crestline Gas &amp; Plumbing – Business Card</title>
<link href="https://fonts.googleapis.com/css2?family=Open+Sans:wght@400;700&family=Signika:wght@600&family=Titillium+Web:wght@600&display=swap" rel="stylesheet">
<style>
  :root {
    --backdrop: #dcdde0;
    --card-white: #ffffff;
    --navy: #24409a;
    --ink: #444a55;
    --icon-blue: #2b4a9e;
    --amber-top: #fdd50c;
    --amber-mid: #f7a928;
    --amber-bottom: #ec6a3c;
    --white: #ffffff;
  }
  * { margin: 0; padding: 0; box-sizing: border-box; }
  html, body { width: 1200px; height: 1187px; overflow: hidden; }
  body {
    background: var(--backdrop);
    position: relative;
    font-family: "Open Sans", sans-serif;
  }
  .card { position: absolute; left: 288px; width: 626px; height: 359px; }

  .card-front { top: 192px; background: var(--card-white); }
  .holder-name {
    position: absolute; left: 82px; top: 22px;
    font-family: "Signika", sans-serif; font-weight: 600;
    font-size: 24px; color: var(--navy); letter-spacing: 0.2px;
  }
  .holder-title {
    position: absolute; left: 82px; top: 52px;
    font-size: 13px; color: var(--ink);
  }
  .brand-front {
    position: absolute; left: 82px; top: 140px;
    display: flex; align-items: center; gap: 12px;
  }
  .brand-mark { width: 30px; height: 30px; border-radius: 50%; background: var(--navy); }
  .brand-name {
    font-family: "Open Sans", sans-serif; font-weight: 700;
    font-size: 30px; color: var(--navy); letter-spacing: 0.5px;
  }
  .contact-list {
    position: absolute; left: 82px; top: 243px; list-style: none;
  }
  .contact-list li {
    display: flex; align-items: center; gap: 6px;
    font-size: 13px; color: var(--ink); height: 23.5px;
  }
  .contact-list li.phone { font-size: 14px; }
  .contact-list svg { width: 15px; height: 15px; flex: none; }

  .card-back {
    top: 637px;
    background: linear-gradient(180deg, var(--amber-top) 0%, var(--amber-mid) 55%, var(--amber-bottom) 100%);
  }
  .brand-back {
    position: absolute; left: 0; right: 0; top: 135px;
    display: flex; justify-content: center; align-items: center; gap: 12px;
  }
  .brand-back .brand-mark { background: var(--white); }
  .brand-back .brand-name { color: var(--white); font-size: 34px; }
  .tagline {
    position: absolute; left: 0; right: 0; top: 275px;
    text-align: center; font-family: "Titillium Web", sans-serif; font-weight: 600;
    font-size: 15px; line-height: 18px; color: var(--white); text-transform: uppercase;
  }
</style>
</head>
<body>
  <section class="card card-front">
    <h1 class="holder-name">Dale Whitcombe</h1>
    <p class="holder-title">Director</p>
    <div class="brand-front">
      <span class="brand-mark"></span>
      <span class="brand-name">Crestline Gas &amp; Plumbing</span>
    </div>
    <ul class="contact-list">
      <li>
        <svg viewBox="0 0 16 16"><path d="M8 1a5 5 0 0 0-5 5c0 3.5 5 9 5 9s5-5.5 5-9a5 5 0 0 0-5-5z" fill="none" stroke="var(--icon-blue)" stroke-width="1.6"/><circle cx="8" cy="6" r="1.8" fill="var(--icon-blue)"/></svg>
        w. Marlowe Ave Suite California Fresno, 93710
      </li>
      <li class="phone">
        <svg viewBox="0 0 16 16"><path d="M3 1.5l3 .5 1 3.5-1.8 1.3a9 9 0 0 0 4 4l1.3-1.8 3.5 1 .5 3c-.5 1-1.5 1.5-2.5 1.5C6.5 14.5 1.5 9.5 1.5 4 1.5 3 2 2 3 1.5z" fill="var(--icon-blue)"/></svg>
        0455163027
      </li>
      <li>
        <svg viewBox="0 0 16 16"><rect x="1" y="3" width="14" height="10" fill="var(--icon-blue)"/><path d="M1 3l7 5.5L15 3M1 13l5-5M15 13l-5-5" fill="none" stroke="#fff" stroke-width="1.2"/></svg>
        admin@crestlinegasandplumbing.example.com.au
      </li>
      <li>
        <svg viewBox="0 0 16 16" fill="none" stroke="var(--icon-blue)" stroke-width="1.1"><circle cx="8" cy="8" r="6.5"/><ellipse cx="8" cy="8" rx="3" ry="6.5"/><path d="M1.5 8h13M2.5 4.8h11M2.5 11.2h11"/></svg>
        www.crestlinegasandplumbing.example.com.au
      </li>
    </ul>
  </section>

  <section class="card card-back">
    <div class="brand-back">
      <span class="brand-mark"></span>
      <span class="brand-name">Crestline Gas &amp; Plumbing</span>
    </div>
    <p class="tagline">All types of plumbing and gas work<br>and specialise in general maintenance plumbing</p>
  </section>
</body>
</html>
```